Positive Psychology and Coaching Web Design Project

I am a trained psychologist and need to develop a website for my positive life coaching and positive psychology training business. My business is based on Positive Psychology, which is the science of human performance enhancement, to help people reach their potential and flourish in their lives. I work with both individuals, and groups in both businesses and schools helping people improve and create more positive, authentic and successful lives by enhancing their performance and improving their wellbeing, resilience, happiness and quality of life.
The business name: My company is named after a fruit, the pomegranate, which is a very special super fruit, with health enhancing benefits and it is a symbol for growth and positive relationships. The pomegranate is full of many seeds, which represent potential, possibilities and ideas.
The website should have integrity, be professional, strong, inspiring and authentic.

Target Market(s)

I coach and work with executives, individuals and children one-on-one, and also teach and train groups in both businesses and schools. The website needs to be professional, in order to fit into the corporate world of executive coaching, but also friendly and inspiring to fit in with positive education in schools.

Industry/Entity Type

Life Coaching

Font styles to use
Sans Serif

Requirements
Must have
• Use of my logo, however, it is flexible how it is used, and the designer can choose which version to use. There is a closed pomegranate with leaves, an open pomegranate to show seeds with leaves, and both of these without leaves.
See attached files:
File 1: A.png: preferred version used on back of business card
File 4: B.png: preferred version but not used anywhere yet, but goes nicely with A?
File 3: C.png: open pomegranate with seeds used on text side of business card
File 2: D.png: plain pomegranate, could be used as a bullet point??!

A home page with toggle buttons to go to other pages such as:
Home
About
Individuals & Organisations
Young People & Schools
Resources
Contact
Nice to have
• The pomegranate is full of many seeds, which represent potential, possibilities and ideas. My logo has a version with the closed pomegranate, and one with the open pomegranate revealing the seeds. Both these could be used on the website, perhaps clicking on the closed pomegranate to reveal the seeds??! My business card has the closed pomegranate on the back and the open seed pomegranate on the side with my name and details. I trust the designer to choose professional suitable colours, however, I do like the colours used on my logo and business card and the consistency might be nice, these colours are:
Pomegranate Red Colour C:24.67%, M: 100%, Y: 100%, K: 24.49%;
Green Writing Colour: C: 71.16%, M: 49.66%, Y: 100%, K: 54.04%
Green Leaf Colour: C: 69.18%, M: 47.02%, Y: 100%, K: 48.21%

```html
<!DOCTYPE html>
<html lang="en">
<head>
<meta charset="utf-8">
<title>Seedwell Coaching — Home</title>
<link rel="stylesheet" href="https://fonts.googleapis.com/css2?family=Arimo:wght@400&family=Tinos:wght@400&family=Archivo+Narrow:wght@400&display=swap">
<style>
  :root {
    --brand-red: #a01408;
    --brand-red-dark: #5a0b04;
    --brand-green: #3f4a1a;
    --menu-muted: #c9c4bf;
    --text-dark: #111111;
    --white: #ffffff;
    --thumb-grey: #cccccc;
    --thumb-border: #6b6b6b;
    --arrow-grey: #6f6f6f;
    --panel-border: #7a7a7a;
  }
  * { box-sizing: border-box; margin: 0; padding: 0; }
  html, body { width: 1200px; height: 1000px; overflow: hidden; background: var(--white); }
  body { position: relative; font-family: "Arimo", Arial, sans-serif; color: var(--text-dark); }

  .brand { position: absolute; left: 28px; top: 22px; width: 390px; height: 100px; }
  .brand-mark { position: absolute; left: 4px; top: 12px; width: 76px; height: 76px; border-radius: 50%; background: var(--brand-red); }
  .brand-name { position: absolute; left: 92px; top: 6px; font-size: 50px; line-height: 1; color: var(--brand-red); letter-spacing: -0.5px; }
  .brand-tag { position: absolute; right: 8px; top: 60px; font-size: 30px; line-height: 1; color: var(--brand-green); }

  .menu-toggle { position: absolute; left: 1078px; top: 50px; width: 88px; height: 48px; }
  .menu-toggle span { position: absolute; left: 0; width: 88px; height: 9px; background: var(--brand-red); }
  .menu-toggle span:nth-child(1) { top: 2px; }
  .menu-toggle span:nth-child(2) { top: 18px; }
  .menu-toggle span:nth-child(3) { top: 38px; }
  .menu-pointer { position: absolute; left: 1098px; top: 110px; }

  .main-nav { position: absolute; left: 31px; top: 137px; width: 1140px; height: 275px; background: var(--brand-red); border: 1px solid #2a0502; }
  .main-nav ul { list-style: none; text-align: center; padding-top: 8px; }
  .main-nav li { font-family: "Tinos", "Times New Roman", serif; font-size: 33px; line-height: 44px; color: var(--white); }
  .main-nav li.is-current { color: var(--menu-muted); }

  .hero { position: absolute; left: 33px; top: 425px; width: 1142px; height: 407px;
    background: linear-gradient(180deg, #cdb89a 0%, #e9dcc4 12%, #f2e4c8 35%, #f3dfb9 55%, #e4c598 75%, #d3ad7c 100%); }
  .hero-caption { position: absolute; left: 589px; top: 100px; width: 550px; height: 232px;
    background: rgba(255,255,255,0.35); border: 1px solid var(--panel-border); }
  .hero-caption p { position: absolute; left: 20px; top: 38px; width: 525px; font-size: 24px; line-height: 43px; letter-spacing: -0.3px; }
  .read-more { position: absolute; left: 403px; top: 153px; width: 118px; height: 42px; border-radius: 21px;
    background: var(--brand-red); border: 1px solid #2a0502; color: var(--white);
    font-family: "Archivo Narrow", "Arial Narrow", sans-serif; font-size: 25px; line-height: 40px; text-align: center; }
  .slide-dots { position: absolute; left: 1062px; top: 386px; display: flex; gap: 6px; }
  .slide-dots span { width: 13px; height: 13px; border-radius: 50%; background: var(--brand-red); border: 1px solid #333; }
  .slide-dots span.is-active { background: var(--white); }

  .clients-title { position: absolute; left: 33px; top: 872px; font-size: 34px; line-height: 1; color: var(--brand-green); }
  .client-logo { position: absolute; width: 160px; height: 79px; background: var(--thumb-grey); border: 1px solid var(--thumb-border); }
  .carousel-arrow { position: absolute; width: 50px; height: 62px; }

  .copyright { position: absolute; left: 36px; top: 970px; font-size: 19px; }
  .social-link { position: absolute; top: 946px; width: 46px; height: 46px; border-radius: 6px; }
  .social-link.one { left: 1008px; background: #3b5a98; }
  .social-link.two { left: 1071px; background: #3fa9dd; }
  .social-link.three { left: 1131px; background: #c8232c; }
</style>
</head>
<body>
  <header>
    <div class="brand">
      <span class="brand-mark"></span>
      <span class="brand-name">Seedwell</span>
      <span class="brand-tag">Coaching</span>
    </div>
    <div class="menu-toggle" aria-label="Toggle menu"><span></span><span></span><span></span></div>
    <svg class="menu-pointer" width="40" height="28" viewBox="0 0 40 28" aria-hidden="true">
      <polyline points="3,26 20,5 37,26" fill="none" stroke="#b3362a" stroke-width="5"/>
    </svg>
    <nav class="main-nav">
      <ul>
        <li class="is-current">Home</li>
        <li>About</li>
        <li>Individuals &amp; Organisations</li>
        <li>Young People &amp; Schools</li>
        <li>Resources</li>
        <li>Contact</li>
      </ul>
    </nav>
  </header>

  <main>
    <section class="hero" role="img" aria-label="Photo of a person meditating cross-legged on a sunlit beach at sunset">
      <div class="hero-caption">
        <p>Lorem ipsum dolor sit amet, consectetur adipiscing elit,sed do eiusmod tempor incididunt.</p>
        <span class="read-more">Read More..</span>
      </div>
      <div class="slide-dots"><span class="is-active"></span><span></span><span></span><span></span></div>
    </section>

    <section class="clients">
      <h2 class="clients-title" style="font-weight:400">Who Worked WithUs:</h2>
      <div class="client-logo" style="left:416px;top:855px"></div>
      <div class="client-logo" style="left:609px;top:853px"></div>
      <div class="client-logo" style="left:802px;top:852px"></div>
      <div class="client-logo" style="left:995px;top:849px"></div>
      <svg class="carousel-arrow" style="left:387px;top:859px" viewBox="0 0 50 62" aria-label="Previous">
        <ellipse cx="25" cy="31" rx="24" ry="30" fill="#6f6f6f" fill-opacity="0.85" stroke="#444"/>
        <polyline points="34,20 12,31 34,42" fill="none" stroke="#e6e6e6" stroke-width="2"/>
      </svg>
      <svg class="carousel-arrow" style="left:1133px;top:856px" viewBox="0 0 50 62" aria-label="Next">
        <ellipse cx="25" cy="31" rx="24" ry="30" fill="#6f6f6f" fill-opacity="0.85" stroke="#444"/>
        <polyline points="16,20 38,31 16,42" fill="none" stroke="#e6e6e6" stroke-width="2"/>
      </svg>
    </section>
  </main>

  <footer>
    <p class="copyright">Copyright 2015. All Rights Reserved.</p>
    <span class="social-link one" aria-label="Social profile"></span>
    <span class="social-link two" aria-label="Social profile"></span>
    <span class="social-link three" aria-label="Social profile"></span>
  </footer>
</body>
</html>
```